Stationary for Prime Counsel Guild

I need stationary for Prime Counsel Guild which
uses our logo
uses our address at:

3182 Maple Terrace
Suite 410
Las Vegas, Nevada 89047

uses our phone number:
(866)HELM402
(866)435-6402

Classy Design with Power and Integrity
I ALSO NEED A SECOND SHEET FOR LETTERS
AND
A 10" by 13" ENVELOPE
AS WELL AS REGULAR ENVELOPE

AND
A 10" by 13" ENVELOPE

uses our website:
www.PrimeCounselGuild.example

uses our email address
info@PrimeCounselGuild.example
Updates

AND

A 10" by 13" ENVELOPE

                                   

                               

AND

A 10" by 13" ENVELOPE

                                   

Please make sure that you have used the latest updated logo supplied in brief on this project.  Also please make sure that the logo AND the words PRIME COUNSEL GUILD is prominent on th etop of letterhead.  I look forwrad to your editions.  Walter Dunmore President

Update: Please use the updated logo on the letterhead and envelopes.  I want the LOGO prominant and centered at the top of page with PRIME COUNSEL GUILD (Use Traditional and powerful font similar to Georgian or like in power and tradition) under it with address, telephone, email and wedsite information.  I also want a second page for letter with similar look but no logo in top of page with info at bottom of second page.  I will make a decide on design quickly.  Thank you vesy much.

Reason: Update: Please use the updated logo on the letterhead and envelopes. I want the LOGO prominant and centered at the top of page with PRIME COUNSEL GUILD (Use Traditional and powerful font similar to Georgian or like in power and tradition) under it with address, telephone, email and wedsite information. I also want a second page for letter with similar look but no logo in top of page with info at bottom of second page. I will make a decide on design quickly. Thank you vesy much.

Target Market(s)

Attorneys invited to join organization.

Requirements
Must have
• Classy Design with Power and Integrity
AND
A 10" by 13" ENVELOPE

Update: Please use the updated logo on the letterhead and envelopes. I want the LOGO prominant and centered at the top of page with PRIME COUNSEL GUILD (Use Traditional and powerful font similar to Georgian or like in power and tradition) under it with address, telephone, email and wedsite information. I also want a second page for letter with similar look but no logo in top of page with info at bottom of second page. I will make a decide on design quickly. Thank you vesy much.
Nice to have
AND
A 10" by 13" ENVELOPE
Should not have
• Nothing casual or funny

```html
<!DOCTYPE html>
<html lang="en">
<head>
<meta charset="utf-8">
<title>Prime Counsel Guild — Stationery Suite</title>
<link href="https://fonts.googleapis.com/css2?family=Cinzel:wght@400;700&display=swap" rel="stylesheet">
<style>
  :root{
    --bg:#bfc0c2;
    --paper:#ffffff;
    --crimson:#b3121c;
    --crimson-dark:#6e0a10;
    --gold:#9a6a1c;
    --gold-light:#c9a45a;
    --ink:#2a2a2a;
    --card-black:#141414;
    --window:#e4e4e4;
  }
  *{box-sizing:border-box;margin:0;padding:0}
  html,body{width:1200px;height:1000px;overflow:hidden}
  body{background:var(--bg);font-family:"Cinzel",Georgia,serif;color:var(--ink);position:relative}
  .piece{position:absolute;background:var(--paper);box-shadow:0 3px 10px rgba(0,0,0,.25);overflow:hidden}
  .piece > svg.bands{position:absolute;inset:0;width:100%;height:100%}
  .mark{display:block;border-radius:50%;background:var(--crimson)}
  .brand{color:var(--crimson);font-weight:700;letter-spacing:.04em;white-space:nowrap}

  /* Letterhead */
  .letterhead{left:40px;top:40px;width:340px;height:440px}
  .second-sheet{left:420px;top:40px;width:340px;height:440px}
  .lh-mark{position:absolute;left:152px;top:10px;width:36px;height:36px}
  .lh-brand{position:absolute;left:0;right:0;top:50px;text-align:center;font-size:8px}
  .letter-body{position:absolute;left:34px;right:34px;top:74px;font-size:6.2px;line-height:1.5}
  .second-sheet .letter-body{top:52px}
  .letter-body h3{font-size:6.6px;font-weight:700;margin-top:5px}
  .letter-body p{margin-top:2px}
  .lh-foot{position:absolute;left:20px;right:20px;bottom:22px;text-align:center;font-size:4.6px;letter-spacing:.02em;color:#555}
  .lh-foot-mark{position:absolute;right:22px;bottom:36px;width:18px;height:18px}

  /* 10 x 13 envelope */
  .catalog-envelope{left:800px;top:40px;width:340px;height:440px}
  .ce-head{position:absolute;left:70px;top:16px;display:flex;gap:6px;align-items:flex-start}
  .ce-head .mark{width:30px;height:30px;flex:none}
  .return-address{font-size:6px;line-height:1.35}
  .return-address .brand{font-size:7px}
  .ce-window{position:absolute;right:22px;top:30px;width:118px;height:34px;border-radius:6px;background:var(--window);border:1px solid #cfcfcf}
  .ghost-seal{position:absolute;left:140px;top:150px;width:260px;height:260px;border-radius:50%;border:14px solid rgba(179,18,28,.07);display:flex;align-items:center;justify-content:center}
  .ghost-seal span{font-size:18px;font-weight:700;color:rgba(179,18,28,.09);letter-spacing:.05em;transform:translateX(-40px);white-space:nowrap}

  /* Business envelope */
  .envelope{top:520px;width:440px;height:190px}
  .envelope.one{left:130px}
  .envelope.two{left:630px}
  .env-head{position:absolute;left:30px;top:12px;display:flex;gap:6px;align-items:flex-start}
  .env-head .mark{width:26px;height:26px;flex:none}
  .env-window{position:absolute;left:70px;top:96px;width:200px;height:56px;border-radius:8px;background:var(--window);border:1px solid #cfcfcf}

  /* Business cards */
  .card{top:750px;width:250px;height:143px}
  .card.front-a{left:55px}
  .card.back-a{left:345px;background:var(--card-black)}
  .card.front-b{left:635px}
  .card.back-b{left:925px;background:var(--card-black)}
  .card-mark{position:absolute;left:26px;top:14px;width:30px;height:30px}
  .card-name{position:absolute;right:16px;top:22px;text-align:right}
  .card-name strong{display:block;color:var(--crimson);font-size:10px;font-weight:700}
  .card-name span{font-size:7px}
  .card-contact{position:absolute;left:26px;bottom:14px;font-size:6px;line-height:1.4}
  .card-contact .web{color:var(--crimson)}
  .back-seal{position:absolute;left:0;right:0;top:24px;display:flex;flex-direction:column;align-items:center;gap:8px}
  .back-seal .mark{width:58px;height:58px;border:3px solid var(--gold-light)}
  .back-seal .brand{font-size:10px;color:var(--gold-light)}
  .back-web{position:absolute;left:0;right:0;bottom:12px;text-align:center;font-size:6.5px;color:var(--crimson)}
</style>
</head>
<body>

<!-- Letterhead, first sheet -->
<section class="piece letterhead">
  <svg class="bands" viewBox="0 0 340 440" preserveAspectRatio="none" aria-hidden="true">
    <polygon points="0,16 150,16 140,28 0,28" fill="var(--gold)"/>
    <polygon points="190,0 340,0 340,14 178,14" fill="var(--crimson)"/>
    <rect x="0" y="36" width="340" height="1.5" fill="var(--gold)"/>
    <rect x="0" y="396" width="340" height="1" fill="var(--gold)"/>
    <polygon points="0,420 340,408 340,424 0,436" fill="var(--gold)"/>
    <polygon points="0,428 340,416 340,440 0,440" fill="var(--crimson)"/>
  </svg>
  <span class="mark lh-mark"></span>
  <div class="brand lh-brand">PRIME COUNSEL GUILD</div>
  <div class="letter-body">
    <h3>Letterhead Design</h3>
    <p>Task Outline</p>
    <p>Create a Letterhead Design</p>
    <h3>Task Description</h3>
    <p>We are a Prime Counsel Guild within an ageing industry. Our industry is responsible for life safety aspects of the built environment. We ensure buildings are safe and fit for occupation.</p>
    <p>We use letterhead and reports everyday. We need a smart and professional letterhead that reflects the serious nature of the work we do. We also require a report template of the same ilk.</p>
    <h3>Deadline</h3>
    <p>Tuesday, December 24, 2013</p>
    <h3>Target Market(s)</h3>
    <p>Our target market will consist mainly of professional architects, developers and construction companies.</p>
    <h3>Look and Feel</h3>
    <p>Each slider illustrates characteristics of the customer's brand and the style your design should communicate.</p>
    <p>I need stationary for Prime Counsel Guild which uses our logo, uses our address at: classy design with power and integrity. I also need a second sheet for letters and a 10" by 13" envelope as well as regular envelope. Uses our website: www.PrimeCounselGuild.example, uses our email address info@PrimeCounselGuild.example</p>
    <p>Deadline: Tuesday, December 24, 2013</p>
  </div>
  <span class="mark lh-foot-mark"></span>
  <div class="lh-foot">(866)HELM402 | (866)435-6402 | 3182 Maple Terrace, Suite 410, Las Vegas, Nevada 89047 | www.PrimeCounselGuild.example | info@PrimeCounselGuild.example</div>
</section>

<!-- Letterhead, second sheet -->
<section class="piece second-sheet">
  <svg class="bands" viewBox="0 0 340 440" preserveAspectRatio="none" aria-hidden="true">
    <polygon points="0,16 150,16 140,28 0,28" fill="var(--gold)"/>
    <polygon points="190,0 340,0 340,14 178,14" fill="var(--crimson)"/>
    <rect x="0" y="36" width="340" height="1.5" fill="var(--gold)"/>
    <rect x="0" y="396" width="340" height="1" fill="var(--gold)"/>
    <polygon points="0,420 340,408 340,424 0,436" fill="var(--gold)"/>
    <polygon points="0,428 340,416 340,440 0,440" fill="var(--crimson)"/>
  </svg>
  <div class="letter-body">
    <h3>Letterhead Design</h3>
    <p>Task Outline</p>
    <p>Create a Letterhead Design</p>
    <h3>Task Description</h3>
    <p>We are a Prime Counsel Guild within an ageing industry. Our industry is responsible for life safety aspects of the built environment. We ensure buildings are safe and fit for occupation.</p>
    <p>We use letterhead and reports everyday. We need a smart and professional letterhead that reflects the serious nature of the work we do.</p>
  </div>
  <span class="mark lh-foot-mark"></span>
  <div class="lh-foot">(866)HELM402 | (866)435-6402 | 3182 Maple Terrace, Suite 410, Las Vegas, Nevada 89047 | www.PrimeCounselGuild.example | info@PrimeCounselGuild.example</div>
</section>

<!-- 10" x 13" envelope -->
<section class="piece catalog-envelope">
  <svg class="bands" viewBox="0 0 340 440" preserveAspectRatio="none" aria-hidden="true">
    <polygon points="0,0 60,0 60,250 0,290" fill="var(--crimson)"/>
    <polygon points="0,300 60,260 60,266 0,306" fill="var(--gold-light)"/>
    <polygon points="0,312 60,272 60,440 0,440" fill="var(--gold)"/>
  </svg>
  <div class="ghost-seal"><span>PRIME COUNSEL GUILD</span></div>
  <div class="ce-head">
    <span class="mark"></span>
    <div class="return-address">
      <div class="brand">Prime Counsel Guild</div>
      <div>3182 Maple Terrace</div>
      <div>Suite 410</div>
      <div>Las Vegas, Nevada 89047</div>
    </div>
  </div>
  <div class="ce-window"></div>
</section>

<!-- Business envelopes -->
<section class="piece envelope one">
  <svg class="bands" viewBox="0 0 440 190" preserveAspectRatio="none" aria-hidden="true">
    <polygon points="0,0 20,0 20,110 0,130" fill="var(--crimson)"/>
    <polygon points="0,136 20,116 20,120 0,140" fill="var(--gold-light)"/>
    <polygon points="0,146 20,126 20,190 0,190" fill="var(--gold)"/>
  </svg>
  <div class="env-head">
    <span class="mark"></span>
    <div class="return-address">
      <div class="brand">Prime Counsel Guild</div>
      <div>3182 Maple Terrace</div>
      <div>Suite 410</div>
      <div>Las Vegas, Nevada 89047</div>
    </div>
  </div>
  <div class="env-window"></div>
</section>

<section class="piece envelope two">
  <svg class="bands" viewBox="0 0 440 190" preserveAspectRatio="none" aria-hidden="true">
    <polygon points="0,0 20,0 20,110 0,130" fill="var(--crimson)"/>
    <polygon points="0,136 20,116 20,120 0,140" fill="var(--gold-light)"/>
    <polygon points="0,146 20,126 20,190 0,190" fill="var(--gold)"/>
  </svg>
  <div class="env-head">
    <span class="mark"></span>
    <div class="return-address">
      <div class="brand">Prime Counsel Guild</div>
      <div>3182 Maple Terrace</div>
      <div>Suite 410</div>
      <div>Las Vegas, Nevada 89047</div>
    </div>
  </div>
  <div class="env-window"></div>
</section>

<!-- Business cards -->
<section class="piece card front-a">
  <svg class="bands" viewBox="0 0 250 143" preserveAspectRatio="none" aria-hidden="true">
    <polygon points="0,0 14,0 14,80 0,94" fill="var(--crimson)"/>
    <polygon points="0,100 14,86 14,90 0,104" fill="var(--gold-light)"/>
    <polygon points="0,110 14,96 14,143 0,143" fill="var(--gold)"/>
  </svg>
  <span class="mark card-mark"></span>
  <div class="card-name"><strong>Walter Dunmore, Esq.</strong><span>Attorney of Law</span></div>
  <div class="card-contact">
    <div>3182 Maple Terrace</div>
    <div>Suite 410</div>
    <div>Las Vegas, Nevada 89047</div>
    <div>(866)HELM402</div>
    <div>(866)435-6402</div>
    <div>info@PrimeCounselGuild.example</div>
    <div class="web">www.PrimeCounselGuild.example</div>
  </div>
</section>

<section class="piece card back-a">
  <div class="back-seal">
    <span class="mark"></span>
    <span class="brand">PRIME COUNSEL GUILD</span>
  </div>
  <div class="back-web">www.PrimeCounselGuild.example</div>
</section>

<section class="piece card front-b">
  <svg class="bands" viewBox="0 0 250 143" preserveAspectRatio="none" aria-hidden="true">
    <polygon points="0,0 14,0 14,80 0,94" fill="var(--crimson)"/>
    <polygon points="0,100 14,86 14,90 0,104" fill="var(--gold-light)"/>
    <polygon points="0,110 14,96 14,143 0,143" fill="var(--gold)"/>
  </svg>
  <span class="mark card-mark"></span>
  <div class="card-name"><strong>Walter Dunmore, Esq.</strong><span>Attorney of Law</span></div>
  <div class="card-contact">
    <div>3182 Maple Terrace</div>
    <div>Suite 410</div>
    <div>Las Vegas, Nevada 89047</div>
    <div>(866)HELM402</div>
    <div>(866)435-6402</div>
    <div>info@PrimeCounselGuild.example</div>
    <div class="web">www.PrimeCounselGuild.example</div>
  </div>
</section>

<section class="piece card back-b">
  <div class="back-seal">
    <span class="mark"></span>
    <span class="brand">PRIME COUNSEL GUILD</span>
  </div>
  <div class="back-web">www.PrimeCounselGuild.example</div>
</section>

</body>
</html>
```